Letterhead Creation

I would like to create a letterhead incorporating my family crest attached. My current letterhead with my information is also attached. I would also like to add my Paralegal Rosalind Merriweather

```html
<!DOCTYPE html>
<html lang="en">
<head>
<meta charset="utf-8">
<title>Letterhead – Law Offices of Jacqueline Vasquez</title>
<link href="https://fonts.googleapis.com/css2?family=Oswald:wght@700&family=Arimo:wght@400&display=swap" rel="stylesheet">
<style>
  :root {
    --backdrop: #000000;
    --paper: #ffffff;
    --navy: #263a8c;
    --crest-blue: #1f4a9e;
    --contact-grey: #8c8c8c;
    --watermark: #e9edf5;
  }
  html, body {
    margin: 0;
    padding: 0;
    width: 1200px;
    height: 1200px;
    overflow: hidden;
    background: var(--backdrop);
  }
  .sheet {
    position: absolute;
    left: 82px;
    top: 190px;
    width: 1118px;
    height: 1010px;
    background: var(--paper);
    overflow: hidden;
  }
  .crest {
    position: absolute;
    left: 94px;
    top: 74px;
    width: 222px;
    height: 232px;
  }
  .watermark-crest {
    position: absolute;
    left: 230px;
    top: 558px;
    width: 840px;
    height: 520px;
  }
  .firm-name {
    position: absolute;
    left: 408px;
    top: 92px;
    margin: 0;
    font-family: "Oswald", "Arial Narrow", sans-serif;
    font-weight: 700;
    font-size: 58px;
    line-height: 1;
    letter-spacing: -0.5px;
    color: var(--navy);
    white-space: nowrap;
  }
  .rule {
    position: absolute;
    left: 409px;
    top: 176px;
    right: 0;
    height: 1.5px;
    background: var(--navy);
  }
  .contact {
    position: absolute;
    top: 210px;
    margin: 0;
    font-family: "Arimo", "Helvetica Neue", Arial, sans-serif;
    font-size: 17px;
    line-height: 21px;
    color: var(--contact-grey);
    font-style: normal;
    white-space: nowrap;
    text-align: right;
  }
  .contact-address {
    right: 202px;
  }
  .contact-lines {
    right: -80px;
  }
</style>
</head>
<body>
  <main class="sheet">
    <svg class="watermark-crest" viewBox="0 0 840 520" role="img" aria-label="Faint family crest watermark with helmet, mantling and shield">
      <defs>
        <radialGradient id="watermarkFade" cx="50%" cy="55%" r="60%">
          <stop offset="0%" stop-color="#eef0f4"/>
          <stop offset="100%" stop-color="#e6ebf4"/>
        </radialGradient>
      </defs>
      <path d="M60 520 C60 300 140 140 240 40 L600 40 C700 140 780 300 780 520 Z" fill="url(#watermarkFade)"/>
    </svg>

    <svg class="crest" viewBox="0 0 222 232" role="img" aria-label="Family crest with knight's helmet, blue mantling and chevron shield">
      <path d="M20 120 C20 60 60 20 111 10 C162 20 202 60 202 120 L202 180 C170 200 150 220 111 232 C72 220 52 200 20 180 Z" fill="var(--crest-blue)"/>
    </svg>

    <h1 class="firm-name">LAW OFFICES OF JACQUELINE VASQUEZ</h1>
    <div class="rule"></div>

    <address class="contact contact-address">
      Jacqueline Vasquez Esq.<br>
      Rosalind Merriweather, Paralegal<br>
      417 N. Alder Ave.<br>
      Glendora, Ca 91740
    </address>

    <address class="contact contact-lines">
      T: 626 555-0148<br>
      F: 626 555-0149<br>
      E: Jacqueline@Vasquezlaw.com
    </address>
  </main>
</body>
</html>
```